Logo + Label Design (Men’s Grooming Brand & Product Packaging)

Design a logo and 2 oz pomade label for Brant, a modern men’s grooming brand focused on clean, high-quality, natural ingredients. The design should establish a bold, masculine, minimalist identity that can later extend to products like shaving gel and body wash.

Key Requirements

Create a primary logo for “Brant” and a core label for the 2 oz pomade jar (screw-top).

Use a clean, modern style — masculine, confident, and approachable (think Wendel’s, Valto, Northfield Mill).

Design for 1–2 color screen printing on solid jar colors (white, black, or navy).

Avoid gradients, foil, or embossing. Must work in black & white.

Provide: vector logo, mockup of the 2 oz jar, color palette (CMYK/RGB/HEX), and font specs.

Winning design may lead to future projects (body wash, shave gel, skincare lines).

Font styles to use
Other font styles liked:
• We like the fonts and design concept in the attached mockup.

Requirements
Should not have
• We want to avoid too much writing or busy designs. We want to avoid having graphics/illustrations embedded in the logo if they will cause the brand to look less classy or sophisticated. We also want the design to look simple and all-American (e.g. Pellham and Stroud, Tall Pine, The BRIM, etc). We’d like to give a Kessler & Dunmore vibe that feels classy and high end.

```html
<!DOCTYPE html>
<html lang="en">
<head>
<meta charset="utf-8">
<title>Brant Packaging Design – 2 oz Hair Pomade</title>
<link rel="stylesheet" href="https://fonts.googleapis.com/css2?family=Cormorant:wght@500;600&family=Raleway:wght@400;600;700&display=swap">
<style>
  :root{
    --board:#6e6e6e;
    --caption:#ececec;
    --white:#ffffff;
    --black:#070707;
    --serif:"Cormorant", "Cormorant Garamond", serif;
    --sans:"Raleway", sans-serif;
  }
  html,body{margin:0;padding:0;overflow:hidden;}
  body{width:1200px;height:900px;background:var(--board);position:relative;font-family:var(--sans);}
  .sheet-title{position:absolute;left:39px;top:24px;margin:0;font:400 19px/1 var(--sans);color:var(--caption);letter-spacing:.01em;}
  .font-spec{position:absolute;right:52px;top:18px;display:flex;align-items:baseline;gap:18px;color:var(--caption);}
  .font-spec__label{font:400 11px/1 var(--sans);letter-spacing:.04em;margin-right:2px;}
  .font-spec__serif{font:500 31px/1 var(--serif);}
  .font-spec__sans{font:400 25px/1 var(--sans);}
  .piece{position:absolute;display:block;}
  .is-light{color:var(--black);}
  .is-dark{color:var(--white);}
  .lid,.back{width:306px;height:306px;}
  .side{width:430px;height:96px;}
  .col-lid{left:53px;} .col-back{left:384px;} .col-side{left:717px;}
  .row-top.lid,.row-top.back{top:120px;} .row-bottom.lid,.row-bottom.back{top:473px;}
  .row-top.side{top:226px;} .row-bottom.side{top:578px;}
  .wordmark{font-family:var(--serif);font-weight:500;}
  .label-caps{font-family:var(--sans);font-weight:700;text-transform:uppercase;}
  .serif-head{font-family:var(--serif);font-weight:600;}
  .caption{position:absolute;top:812px;width:200px;margin:0;text-align:center;font:400 27px/1 var(--sans);color:var(--caption);}
  .caption--lid{left:103px;} .caption--back{left:434px;} .caption--side{left:832px;}
</style>
</head>
<body>
  <h1 class="sheet-title">BRANT PACKAGING DESIGN - 2 OZ HAIR POMADE</h1>
  <div class="font-spec">
    <span class="font-spec__label">FONT</span>
    <span class="font-spec__serif">Cormorant</span>
    <span class="font-spec__sans">Raleway</span>
  </div>

  <!-- Lid, light -->
  <svg class="piece lid col-lid row-top is-light" viewBox="0 0 306 306" aria-label="Lid label, white">
    <defs>
      <path id="lid-top-a" d="M40,153 A113,113 0 0 1 266,153"/>
      <path id="lid-bottom-a" d="M26,153 A127,127 0 0 0 280,153"/>
    </defs>
    <circle cx="153" cy="153" r="153" fill="var(--white)"/>
    <text class="label-caps" font-size="13.5" letter-spacing="2" fill="currentColor"><textPath href="#lid-top-a" startOffset="50%" text-anchor="middle">Hair Pomade</textPath></text>
    <text class="wordmark" x="153" y="172" font-size="88" text-anchor="middle" fill="currentColor">Brant</text>
    <line x1="103" y1="217" x2="203" y2="217" stroke="currentColor" stroke-width="1.2"/>
    <text class="label-caps" x="153" y="231" font-size="10" letter-spacing="1.3" text-anchor="middle" fill="currentColor">Fresh &amp; Clean</text>
    <line x1="103" y1="236" x2="203" y2="236" stroke="currentColor" stroke-width="1.2"/>
    <text class="label-caps" font-size="9.5" letter-spacing="1.2" fill="currentColor"><textPath href="#lid-bottom-a" startOffset="50%" text-anchor="middle">Net Weight <tspan font-size="13">2</tspan> oz. (57g)</textPath></text>
  </svg>

  <!-- Back, light -->
  <svg class="piece back col-back row-top is-light" viewBox="0 0 306 306" aria-label="Back label, white">
    <circle cx="153" cy="153" r="153" fill="var(--white)"/>
    <g fill="currentColor" text-anchor="middle">
      <text class="serif-head" x="155" y="78" font-size="12.5" letter-spacing=".3">DIRECTIONS</text>
      <g class="label-caps" font-size="5.2" letter-spacing=".45">
        <text x="155" y="87">Melt small amount of pomade between hands before massaging</text>
        <text x="155" y="93">into damp hair (for sleeker look) or dry hair (for more texture).</text>
        <text x="155" y="99.5">Style as desired. For external use only. Avoid contact with eyes.</text>
        <text x="155" y="106">If irritation occurs, discontinue use.</text>
      </g>
      <text class="serif-head" x="155" y="143" font-size="12.5" letter-spacing=".3">INGREDIENTS</text>
      <g class="label-caps" font-size="5.2" letter-spacing=".45">
        <text x="155" y="152">Butyrospermum parkii (shea butter), cera alba (beeswax),</text>
        <text x="155" y="158">polyglycerol-3 beeswax (cera bellina), caprylic/capric</text>
        <text x="155" y="164.5">triglyceride (fractionated coconut oil), tocopherol (vitamin E),</text>
        <text x="155" y="171">fragrance (parfum)</text>
      </g>
      <text class="label-caps" x="155" y="210" font-size="5" letter-spacing=".5">Manufactured by</text>
      <text class="wordmark" x="155" y="235" font-size="27">Brant</text>
      <g class="label-caps" font-size="5.2" letter-spacing=".45">
        <text x="155" y="251">Brant Health Products, Harlow, NC 28190</text>
        <text x="155" y="257.5">Visit us at branthealthgoods.com</text>
      </g>
    </g>
  </svg>

  <!-- Side, light -->
  <svg class="piece side col-side row-top is-light" viewBox="0 0 430 96" aria-label="Side band label, white">
    <rect width="430" height="96" fill="var(--white)"/>
    <g fill="currentColor">
      <text class="wordmark" x="65" y="59" font-size="40" text-anchor="middle">Brant</text>
      <g text-anchor="middle">
        <text class="label-caps" x="169" y="34" font-size="7" letter-spacing=".9">Hair Pomade</text>
        <line x1="120" y1="38.5" x2="219" y2="38.5" stroke="currentColor" stroke-width=".8"/>
        <text class="label-caps" x="169" y="52" font-size="10" letter-spacing="1.2">Fresh &amp; Clean</text>
        <line x1="120" y1="56.5" x2="219" y2="56.5" stroke="currentColor" stroke-width=".8"/>
        <text class="label-caps" x="169" y="67" font-size="5.3" letter-spacing=".6">Net Weight <tspan font-size="8">2</tspan> oz. (57g)</text>
        <g class="label-caps" font-size="5.3" letter-spacing=".55">
          <text x="325" y="42">Naturally derived plant &amp; bee-based ingredients</text>
          <text x="325" y="50">Alcohol free, non-irritating</text>
          <text x="325" y="58">Formulated to minimize scalp irritation</text>
        </g>
      </g>
    </g>
  </svg>

  <!-- Lid, dark -->
  <svg class="piece lid col-lid row-bottom is-dark" viewBox="0 0 306 306" aria-label="Lid label, black">
    <defs>
      <path id="lid-top-b" d="M40,153 A113,113 0 0 1 266,153"/>
      <path id="lid-bottom-b" d="M26,153 A127,127 0 0 0 280,153"/>
    </defs>
    <circle cx="153" cy="153" r="153" fill="var(--black)"/>
    <text class="label-caps" font-size="13.5" letter-spacing="2" fill="currentColor"><textPath href="#lid-top-b" startOffset="50%" text-anchor="middle">Hair Pomade</textPath></text>
    <text class="wordmark" x="153" y="172" font-size="88" text-anchor="middle" fill="currentColor">Brant</text>
    <line x1="103" y1="217" x2="203" y2="217" stroke="currentColor" stroke-width="1.2"/>
    <text class="label-caps" x="153" y="231" font-size="10" letter-spacing="1.3" text-anchor="middle" fill="currentColor">Fresh &amp; Clean</text>
    <line x1="103" y1="236" x2="203" y2="236" stroke="currentColor" stroke-width="1.2"/>
    <text class="label-caps" font-size="9.5" letter-spacing="1.2" fill="currentColor"><textPath href="#lid-bottom-b" startOffset="50%" text-anchor="middle">Net Weight <tspan font-size="13">2</tspan> oz. (57g)</textPath></text>
  </svg>

  <!-- Back, dark -->
  <svg class="piece back col-back row-bottom is-dark" viewBox="0 0 306 306" aria-label="Back label, black">
    <circle cx="153" cy="153" r="153" fill="var(--black)"/>
    <g fill="currentColor" text-anchor="middle">
      <text class="serif-head" x="155" y="78" font-size="12.5" letter-spacing=".3">DIRECTIONS</text>
      <g class="label-caps" font-size="5.2" letter-spacing=".45">
        <text x="155" y="87">Melt small amount of pomade between hands before massaging</text>
        <text x="155" y="93">into damp hair (for sleeker look) or dry hair (for more texture).</text>
        <text x="155" y="99.5">Style as desired. For external use only. Avoid contact with eyes.</text>
        <text x="155" y="106">If irritation occurs, discontinue use.</text>
      </g>
      <text class="serif-head" x="155" y="143" font-size="12.5" letter-spacing=".3">INGREDIENTS</text>
      <g class="label-caps" font-size="5.2" letter-spacing=".45">
        <text x="155" y="152">Butyrospermum parkii (shea butter), cera alba (beeswax),</text>
        <text x="155" y="158">polyglycerol-3 beeswax (cera bellina), caprylic/capric</text>
        <text x="155" y="164.5">triglyceride (fractionated coconut oil), tocopherol (vitamin E),</text>
        <text x="155" y="171">fragrance (parfum)</text>
      </g>
      <text class="label-caps" x="155" y="210" font-size="5" letter-spacing=".5">Manufactured by</text>
      <text class="wordmark" x="155" y="235" font-size="27">Brant</text>
      <g class="label-caps" font-size="5.2" letter-spacing=".45">
        <text x="155" y="251">Brant Health Products, Harlow, NC 28190</text>
        <text x="155" y="257.5">Visit us at branthealthgoods.com</text>
      </g>
    </g>
  </svg>

  <!-- Side, dark -->
  <svg class="piece side col-side row-bottom is-dark" viewBox="0 0 430 96" aria-label="Side band label, black">
    <rect width="430" height="96" fill="var(--black)"/>
    <g fill="currentColor">
      <text class="wordmark" x="65" y="59" font-size="40" text-anchor="middle">Brant</text>
      <g text-anchor="middle">
        <text class="label-caps" x="169" y="34" font-size="7" letter-spacing=".9">Hair Pomade</text>
        <line x1="120" y1="38.5" x2="219" y2="38.5" stroke="currentColor" stroke-width=".8"/>
        <text class="label-caps" x="169" y="52" font-size="10" letter-spacing="1.2">Fresh &amp; Clean</text>
        <line x1="120" y1="56.5" x2="219" y2="56.5" stroke="currentColor" stroke-width=".8"/>
        <text class="label-caps" x="169" y="67" font-size="5.3" letter-spacing=".6">Net Weight <tspan font-size="8">2</tspan> oz. (57g)</text>
        <g class="label-caps" font-size="5.3" letter-spacing=".55">
          <text x="325" y="42">Naturally derived plant &amp; bee-based ingredients</text>
          <text x="325" y="50">Alcohol free, non-irritating</text>
          <text x="325" y="58">Formulated to minimize scalp irritation</text>
        </g>
      </g>
    </g>
  </svg>

  <p class="caption caption--lid">Lid</p>
  <p class="caption caption--back">Back</p>
  <p class="caption caption--side">Side</p>
</body>
</html>
```